Revamping and duplicating of existing business card

We are a painting and decorating business based in London and need a couple of business cards made up for the following people.

1. Maribel Osgood
2. Tobias Penrick

Measurements - 85 X 55 mm
Font: Blue highway
Colour: No idea! Would be great to have a pantone for the pink if possible?

I’ve attached all the logos and old artwork etc.
Here are the amendments I would definitely like...

1. Maribel

format mobile number correctly: 07512 368 904

Add title: Decorator
Use: Osgood Decorating Logo
Add twitter logo & @osgooddecor
Add tradevouch logo
Add HFG Logo
Make it all look beautiful/revamp/tweak - whatever you think…

2. Tobias

Decorator

07643 295 581
tobias@osgooddecorating.co.uk
Updates

Hello! Thanks so much for all your designs. This is such a great way to get these things done... Just to clarify, Please do not alter our logo at all. The 'splat' appears on our van, tshirts, quotes etc and is very much part of our branding. Colour scheme: Pink, black and white. Thanks Maribel

Project Deadline Extended
Reason: Not 100% sold on any of the designs so far but very grateful for all the submissions. Keep it simple and quirky please. Thanks Maribel

Industry/Entity Type

Painting

Requirements
Must have
• Pink & Black Colour scheme
Osgood Decorating Logo
Blue Highway font

```html
<!DOCTYPE html>
<html lang="en">
<head>
<meta charset="utf-8">
<title>Osgood Decorating – Business Cards</title>
<link href="https://fonts.googleapis.com/css2?family=Ubuntu:wght@400;500;700&display=swap" rel="stylesheet">
<style>
  :root {
    --pink: #e0106a;
    --black: #1a1a1a;
    --grey: #4a4a4a;
    --white: #ffffff;
    --backdrop: #e9e7e4;
    --badge: #1f3f8f;
  }
  * { box-sizing: border-box; margin: 0; padding: 0; }
  html, body {
    width: 1200px; height: 872px; overflow: hidden;
    background: var(--backdrop);
    font-family: "Ubuntu", Arial, sans-serif;
  }
  .sheet {
    position: relative; width: 1200px; height: 872px;
    display: flex; align-items: center; justify-content: center; gap: 60px;
  }
  .card {
    position: relative; width: 510px; height: 330px; overflow: hidden;
    box-shadow: 0 6px 18px rgba(0,0,0,0.18);
  }

  /* Back of card */
  .card--back { background: var(--pink); }
  .member-strip {
    position: absolute; top: 0; right: 0; width: 250px; height: 78px;
    background: var(--white);
    display: flex; align-items: center; justify-content: space-between;
    padding: 0 18px 0 20px;
  }
  .member-strip__label {
    display: block; font-size: 9px; color: var(--grey); margin-bottom: 3px;
  }
  .member-strip__name {
    font-size: 22px; font-weight: 700; color: var(--pink); letter-spacing: -0.3px;
  }
  .association-badge { width: 42px; height: 46px; }
  .website {
    position: absolute; left: 30px; bottom: 28px;
    font-size: 30px; font-weight: 500; color: var(--white); letter-spacing: 0.2px;
  }

  /* Front of card */
  .card--front { background: var(--white); }
  .contact {
    position: absolute; left: 32px; top: 26px;
  }
  .contact__name {
    font-size: 44px; font-weight: 500; line-height: 0.98; color: var(--black);
    letter-spacing: -0.5px;
  }
  .contact__title {
    font-size: 19px; font-weight: 500; color: var(--pink); margin-top: 4px;
  }
  .contact__details { margin-top: 22px; list-style: none; }
  .contact__details li {
    font-size: 15px; line-height: 1.55; color: var(--grey);
    display: flex; align-items: center; gap: 7px;
  }
  .contact__details .email { color: var(--pink); }
  .handle-mark {
    display: inline-block; width: 12px; height: 12px; background: var(--pink);
  }
  .brand {
    position: absolute; right: 24px; bottom: 26px;
    display: flex; align-items: center; gap: 12px;
  }
  .brand__mark {
    width: 64px; height: 64px; border-radius: 50%; background: var(--pink);
  }
  .brand__name {
    font-size: 26px; font-weight: 700; line-height: 1.0; color: var(--pink);
  }
</style>
</head>
<body>
  <main class="sheet">
    <section class="card card--back" aria-label="Card back">
      <div class="member-strip">
        <div>
          <span class="member-strip__label">Proud members of</span>
          <span class="member-strip__name">tradevouch</span>
        </div>
        <svg class="association-badge" viewBox="0 0 42 46" role="img" aria-label="Trade association membership badge">
          <path d="M2 2 H40 V28 Q40 40 21 44 Q2 40 2 28 Z" fill="var(--badge)"/>
        </svg>
      </div>
      <p class="website">www.osgooddecorating.co.uk</p>
    </section>

    <section class="card card--front" aria-label="Card front">
      <div class="contact">
        <h1 class="contact__name">Maribel<br>Osgood</h1>
        <p class="contact__title">Decorator</p>
        <ul class="contact__details">
          <li>07512 368 904</li>
          <li class="email">maribel@osgooddecorating.co.uk</li>
          <li><span class="handle-mark" aria-hidden="true"></span>@osgooddecor</li>
        </ul>
      </div>
      <div class="brand">
        <span class="brand__mark" aria-hidden="true"></span>
        <span class="brand__name">Osgood<br>Decorating</span>
      </div>
    </section>
  </main>
</body>
</html>
```